Business card design needed

We are 2 artists starting up a studio by the water in Port Ellery ...where we can work and display our art...would like the back ground to be Navy and white stripe...nautical...and the name The Clay Nook to be bold and the main wording...not nautical...if possible thought the A for art could be an easel ...ie the capital A using the cross bar as the platform that paint would be circles of colour....would like the main wording in Black but the easel A in colour
Hope u are able to help
thanku Lorna Vesk
as I will be away in a week for 4 weeks could u please send all info to Jodie Minchens email....she can contact me and we can go ahead asap....

Industry/Entity Type

Artists

Contact Information for Business Card

THE CLAY NOOK

Halloways Dock House
The Bend..41 Kelvane Rd..Larkwood 2199 Port Ellery

Jodi Minchen..0417583091..jodiminchen@mailwave.example
Lorn Vesk...0413862714..lvesk@quillnet.example.au

```html
<!DOCTYPE html>
<html lang="en">
<head>
<meta charset="utf-8">
<title>The Clay Nook — Business Card</title>
<link rel="stylesheet" href="https://fonts.googleapis.com/css2?family=Arimo:wght@400;700&display=swap">
<style>
  :root {
    --backdrop: #b3bca4;
    --card-red: #c0001a;
    --card-red-edge: #8e0012;
    --navy: #184c98;
    --white: #ffffff;
    --ink: #111111;
  }
  * { box-sizing: border-box; margin: 0; padding: 0; }
  html, body {
    width: 1200px;
    height: 900px;
    overflow: hidden;
  }
  body {
    background: var(--backdrop);
    font-family: "Arimo", Arial, sans-serif;
    position: relative;
  }
  .card {
    position: absolute;
    top: 305px;
    width: 460px;
    height: 290px;
    box-shadow: 0 4px 12px rgba(0, 0, 0, 0.28);
  }

  /* Front side: contact details */
  .card-front {
    left: 95px;
    background: var(--card-red);
    border: 1px solid var(--card-red-edge);
    color: var(--white);
    font-size: 14px;
    line-height: 19.5px;
  }
  .contact {
    position: absolute;
  }
  .contact-primary { left: 27px; top: 22px; }
  .contact-secondary { right: 28px; top: 212px; text-align: right; }
  .studio {
    position: absolute;
    left: 0;
    right: 0;
    top: 110px;
    text-align: center;
    font-size: 14.5px;
    line-height: 20.5px;
  }
  .studio-name {
    font-weight: 700;
    font-size: 15.5px;
  }

  /* Back side: nautical stripes with name panel */
  .card-back {
    left: 645px;
    background: repeating-linear-gradient(
      90deg,
      var(--navy) 0 32px,
      var(--white) 32px 46px
    );
  }
  .name-panel {
    position: absolute;
    left: 62px;
    right: 62px;
    top: 82px;
    bottom: 82px;
    background: var(--white);
    display: flex;
    align-items: center;
    justify-content: center;
    gap: 14px;
  }
  .name-mark {
    width: 26px;
    height: 26px;
    background: var(--card-red);
  }
  .name-wordmark {
    font-weight: 700;
    font-size: 30px;
    letter-spacing: 0.5px;
    color: var(--ink);
    white-space: nowrap;
  }
</style>
</head>
<body>
  <article class="card card-front" aria-label="Card front">
    <div class="contact contact-primary">
      <p>Jodi Minchen</p>
      <p>T: 0417583091</p>
      <p>jodiminchen@mailwave.example</p>
    </div>
    <div class="studio">
      <p class="studio-name">THE CLAY NOOK</p>
      <p>Halloways Dock House The Bend</p>
      <p>41 Kelvane Rd.</p>
      <p>Larkwood, 2199 Port Ellery</p>
    </div>
    <div class="contact contact-secondary">
      <p>Lorn Vesk</p>
      <p>T: 0413862714</p>
      <p>lvesk@quillnet.example.au</p>
    </div>
  </article>

  <article class="card card-back" aria-label="Card back">
    <div class="name-panel">
      <span class="name-mark" aria-hidden="true"></span>
      <span class="name-wordmark">THE CLAY NOOK</span>
    </div>
  </article>
</body>
</html>
```